e-commerce store for sport clothing online store "baseball merchandise "web application...

I want to design a UX/UI for my web application website for the online store I will provide you with the following:
1. screen shots of the initial design for the pages>
2. the logo files.
3. The brand guideline file.

the provided files (screen shots) is guideline I want to see CREATIVITY with the UX/UI DESIGN.
PS. PLEASE FOLLOW THE BRANDGUIDE LINE CAREFULLY SPECIALLY THE TYPOGRAPHY & THE COLOR CODES.

PLEASE VISIT THIS WEBSITE brightpin.lumar-qt.com to see more for the screens.

```html
<!DOCTYPE html>
<html lang="en">
<head>
<meta charset="utf-8">
<title>Fieldline Store – Tablet Screens</title>
<link href="https://fonts.googleapis.com/css2?family=Inter:wght@400;500;600;700;800&display=swap" rel="stylesheet">
<style>
:root{
  --bg:#eef0f5;
  --screen:#f8f8fb;
  --card:#ffffff;
  --navy:#1c2a4b;
  --red:#b3102d;
  --pink:#f2395a;
  --green:#4fd167;
  --grey:#d6d8de;
  --muted:#8a8f9c;
  --text:#1d2233;
}
*{box-sizing:border-box;margin:0;padding:0}
html,body{width:775px;height:1200px;overflow:hidden;background:var(--bg);font-family:"Inter",sans-serif;color:var(--text)}
.canvas{position:relative;width:775px;height:1200px}
.screen{position:absolute;width:350px;height:260px;background:var(--screen);border-radius:10px;box-shadow:0 6px 18px rgba(30,40,70,.06);overflow:hidden}
.abs{position:absolute}
.brand{position:absolute;left:50%;top:14px;transform:translateX(-50%);display:flex;align-items:center;gap:4px;font-weight:800;font-size:13px;color:var(--navy);letter-spacing:.5px}
.brand .dot{width:7px;height:7px;border-radius:50%;background:var(--red)}
.brand.big{top:105px;font-size:24px;gap:7px}
.brand.big .dot{width:12px;height:12px}
.loading{position:absolute;left:0;right:0;top:177px;text-align:center;font-size:4.5px;color:var(--navy)}
.icon{position:absolute}
.page-title{position:absolute;left:50px;top:53px;font-size:6px;font-weight:600;display:flex;align-items:center;gap:6px}
.page-title::after{content:"";display:block;height:0.6px;background:var(--grey);width:var(--line,50px)}
.steps{position:absolute;top:50px;left:181px;display:flex;gap:20px}
.step{width:14px;height:14px;border-radius:50%;background:var(--grey);color:#fff;font-size:5px;display:flex;align-items:center;justify-content:center}
.step.on{background:var(--red)}
.card{position:absolute;background:var(--card);border-radius:6px;box-shadow:0 4px 12px rgba(30,40,70,.07)}
.art{position:absolute;border-radius:50%}
.art.hat{background:radial-gradient(circle at 40% 40%,#5f86b0,#3b5e86 60%,#2c4a6d)}
.art.cap{background:linear-gradient(160deg,#4a4a5e,#1d1d2b);border-radius:40% 40% 20% 20%}
.art.shirt-w{background:linear-gradient(#f4f4f4,#dcdcdc);border-radius:6px}
.art.shirt-b{background:linear-gradient(#2a2a2a,#111);border-radius:6px}
.row-title{font-size:5px;font-weight:600}
.row-sub{font-size:3.4px;color:#333;margin-top:1px}
.price-sm{position:absolute;right:13px;font-size:5.5px;font-weight:600}
.badge{position:absolute;background:var(--pink);color:#fff;font-size:4px;font-weight:600;border-radius:7px;padding:2.5px 5px;white-space:nowrap}
.qty{position:absolute;width:20px;height:60px;background:var(--grey);border-radius:10px;display:flex;flex-direction:column;align-items:center;justify-content:space-between;padding:3px 0;color:var(--navy);font-size:7px;font-weight:700}
.qty .num{width:20px;height:22px;border-radius:10px;background:var(--navy);color:#fff;display:flex;align-items:center;justify-content:center;font-size:6.5px}
.btn{position:absolute;height:19px;border-radius:10px;background:var(--navy);color:#fff;font-size:4.6px;font-weight:600;letter-spacing:.3px;display:flex;align-items:center;justify-content:space-between;padding:0 5px 0 11px;box-shadow:0 4px 8px rgba(28,42,75,.25)}
.btn svg{width:7px;height:7px}
.title-md{font-size:7.5px;font-weight:600}
.desc{font-size:3.6px;line-height:1.3;color:#333}
.price-lg{font-size:8px;font-weight:700;letter-spacing:.3px}
.field{position:absolute;height:22px;border:0.7px solid var(--grey);border-radius:3px;background:#fff}
.field label{position:absolute;left:5px;top:3px;font-size:2.8px;color:var(--muted);letter-spacing:.2px}
.field label b{color:var(--red);margin-left:3px}
.field span{position:absolute;left:5px;bottom:3px;font-size:7px}
.field .ph{font-size:5.5px;color:var(--muted);top:50%;bottom:auto;transform:translateY(-50%)}
.dropdown{position:absolute;left:263px;top:41px;width:57px;height:16px;border:0.8px solid var(--navy);border-radius:3px;font-size:5.5px;font-weight:500;display:flex;align-items:center;justify-content:space-between;padding:0 5px 0 9px}
.blur{filter:blur(2.5px)}
</style>
</head>
<body>
<div class="canvas">

  <!-- Loading screen -->
  <section class="screen" style="left:25px;top:150px">
    <div class="brand big"><span class="dot"></span>FIELDLINE</div>
    <p class="loading">Loading...</p>
  </section>

  <!-- Product list -->
  <section class="screen" style="left:400px;top:150px">
    <svg class="icon" style="left:14px;top:20px" width="10" height="6" viewBox="0 0 10 6"><path d="M0 .5h10M0 3h7M0 5.5h4" stroke="#1c2a4b" stroke-width="1"/></svg>
    <div class="brand"><span class="dot"></span>FIELDLINE</div>
    <svg class="icon" style="left:317px;top:18px" width="13" height="13" viewBox="0 0 13 13"><path d="M1 5h10l-1.3 6H2.3z M3.5 5l2-3.5M8.5 5l-2-3.5" fill="none" stroke="#1c2a4b" stroke-width=".9"/><circle cx="11.5" cy="1.6" r="1.6" fill="#f2395a"/></svg>
    <div class="dropdown">Marlin<svg width="5" height="3" viewBox="0 0 5 3"><path d="M.5.5l2 2 2-2" fill="none" stroke="#1c2a4b" stroke-width=".7"/></svg></div>

    <div class="card" style="left:28px;top:62px;width:292px;height:38px">
      <div class="art cap" role="img" aria-label="Product photo: dark trucker hat" style="left:4px;top:4px;width:40px;height:32px"></div>
      <div class="abs" style="left:60px;top:14px"><p class="row-title">Salty Marlin Logo Hat</p><p class="row-sub">Step out in style in the marlin hat - Salty Marlin Logo in front</p></div>
      <span class="price-sm" style="top:16px">12,000 KD</span>
    </div>
    <div class="card" style="left:28px;top:113px;width:292px;height:38px">
      <div class="art shirt-w" role="img" aria-label="Product photo: white printed tee" style="left:5px;top:3px;width:34px;height:34px"></div>
      <div class="abs" style="left:60px;top:14px"><p class="row-title">Delta Flyline</p><p class="row-sub">If you don't have one yourself, you know someone with Labrador.</p></div>
      <span class="price-sm" style="top:16px">19,000 KD</span>
    </div>
    <div class="card" style="left:28px;top:165px;width:292px;height:38px">
      <div class="art shirt-b" role="img" aria-label="Product photo: black printed tee" style="left:5px;top:2px;width:34px;height:36px"></div>
      <div class="abs" style="left:60px;top:14px"><p class="row-title">Lagoon Wave Crew</p><p class="row-sub">Turn heads in the Lagoon Wave Crew Tee</p></div>
      <span class="price-sm" style="top:16px">19,000 KD</span>
    </div>
    <div class="card" style="left:28px;top:216px;width:292px;height:38px">
      <div class="art hat" role="img" aria-label="Product photo: blue patterned boonie hat" style="left:4px;top:5px;width:42px;height:30px"></div>
      <div class="abs" style="left:60px;top:14px"><p class="row-title">Reef Boonie Hat</p><p class="row-sub">The Reef Boonie Hat Can handle whatever your day has in store for your Shinny day</p></div>
      <span class="price-sm" style="top:14px">22,000 KD</span>
      <span class="badge" style="right:14px;top:25px;padding:1.5px 4px;font-size:3.4px">20% OFF</span>
    </div>
  </section>

  <!-- Product details -->
  <section class="screen" style="left:25px;top:440px">
    <svg class="icon" style="left:14px;top:23px" width="10" height="6" viewBox="0 0 10 6"><path d="M0 .5h10M0 3h7M0 5.5h4" stroke="#1c2a4b" stroke-width="1"/></svg>
    <div class="brand"><span class="dot"></span>FIELDLINE</div>
    <svg class="icon" style="left:319px;top:20px" width="13" height="13" viewBox="0 0 13 13"><path d="M1 5h10l-1.3 6H2.3z M3.5 5l2-3.5M8.5 5l-2-3.5" fill="none" stroke="#1c2a4b" stroke-width=".9"/><circle cx="11.5" cy="1.6" r="1.6" fill="#f2395a"/></svg>
    <p class="page-title" style="--line:68px">Product Details</p>
    <svg class="abs" style="left:0;top:107px" width="19" height="40" viewBox="0 0 19 40"><path d="M0 0l19 20L0 40z" fill="#1c2a4b"/><path d="M10 17l-3 3 3 3z" fill="#fff"/></svg>
    <svg class="abs" style="left:331px;top:107px" width="19" height="40" viewBox="0 0 19 40"><path d="M19 0L0 20l19 20z" fill="#a4acbb"/><path d="M11 17l3 3-3 3z" fill="#fff"/></svg>
    <div class="card" style="left:50px;top:73px;width:248px;height:130px">
      <div class="art hat" role="img" aria-label="Product photo: blue patterned boonie hat with chin cord" style="left:10px;top:8px;width:96px;height:70px"></div>
      <div class="abs" style="left:119px;top:14px;width:110px">
        <p class="title-md">Reef Boonie Hat</p>
        <p class="desc" style="margin-top:1px">The Reef Boonie Hat Can handle whatever your day has in store for you. Featuring a 360-degree brim and cinchable cord to create a stay-put fit. Available in ink Teal. Hand drawn artwork.</p>
        <p class="desc" style="margin-top:4px">- 100% Polyester<br>- Structured<br>- 6 Panels<br>- SnapBack Closure</p>
        <p class="desc" style="margin-top:4px;color:var(--red)">** This product is one size</p>
      </div>
      <p class="price-lg abs" style="left:119px;top:103px">22,000 KD</p>
    </div>
    <div class="qty" style="left:271px;top:138px"><span>–</span><span class="num">2</span><span>+</span></div>
    <span class="badge" style="left:45px;top:194px">20% OFF</span>
    <div class="btn" style="left:219px;top:218px;width:71px">ADD TO CART<svg viewBox="0 0 10 10"><circle cx="5" cy="5" r="4.3" fill="none" stroke="#fff" stroke-width=".9"/><path d="M3 5h4M5.3 3.3L7 5 5.3 6.7" fill="none" stroke="#fff" stroke-width=".9"/></svg></div>
  </section>

  <!-- Shopping cart -->
  <section class="screen" style="left:400px;top:440px">
    <svg class="icon" style="left:13px;top:23px" width="11" height="7" viewBox="0 0 11 7"><path d="M11 3.5H1M3.5 1L1 3.5 3.5 6" fill="none" stroke="#1c2a4b" stroke-width=".9"/></svg>
    <div class="brand"><span class="dot"></span>FIELDLINE</div>
    <svg class="icon" style="left:319px;top:20px" width="13" height="13" viewBox="0 0 13 13"><path d="M1 5h10l-1.3 6H2.3z M3.5 5l2-3.5M8.5 5l-2-3.5" fill="none" stroke="#1c2a4b" stroke-width=".9"/><circle cx="11.5" cy="1.6" r="1.6" fill="#f2395a"/></svg>
    <p class="page-title" style="--line:68px">Shopping Cart</p>
    <div class="steps"><span class="step on">1</span><span class="step">2</span><span class="step">3</span><span class="step">4</span></div>
    <div class="card" style="left:50px;top:73px;width:248px;height:68px">
      <div class="art hat" role="img" aria-label="Product photo: blue patterned boonie hat" style="left:11px;top:12px;width:42px;height:30px"></div>
      <div class="abs" style="left:88px;top:14px;width:110px">
        <p class="title-md">Reef Boonie Hat</p>
        <p class="desc">The Reef Boonie Hat Can handle whatever your day has in store for you.</p>
      </div>
      <p class="price-lg abs" style="left:88px;top:42px">22,000 KD</p>
    </div>
    <div class="qty" style="left:271px;top:76px"><span>–</span><span class="num">2</span><span>+</span></div>
    <span class="badge" style="left:45px;top:129px">20% OFF</span>
    <div class="card blur" style="left:22px;top:154px;width:252px;height:66px" aria-hidden="true">
      <div class="art hat" style="left:8px;top:18px;width:44px;height:28px"></div>
      <div class="abs" style="left:80px;top:18px;width:80px;height:3px;background:#6a7690"></div>
      <div class="abs" style="left:80px;top:26px;width:110px;height:2px;background:#8d97aa"></div>
      <div class="abs" style="left:80px;top:45px;width:50px;height:3px;background:#5a6680"></div>
      <div class="abs" style="left:216px;top:6px;width:14px;height:54px;border-radius:7px;background:#34456a"></div>
    </div>
    <div class="abs" style="left:298px;top:152px;width:37px;height:68px;border-radius:6px;background:var(--pink);display:flex;align-items:center;justify-content:center">
      <svg width="12" height="13" viewBox="0 0 12 13"><path d="M1 3h10M4 3V1.5h4V3M2.3 3l.7 9h6l.7-9M5 5.5v4.5M7 5.5v4.5" fill="none" stroke="#fff" stroke-width=".9"/></svg>
    </div>
    <div class="btn" style="left:235px;top:232px;width:63px">CHECKOUT<svg viewBox="0 0 10 10"><circle cx="5" cy="5" r="4.3" fill="none" stroke="#fff" stroke-width=".9"/><path d="M3 5h4M5.3 3.3L7 5 5.3 6.7" fill="none" stroke="#fff" stroke-width=".9"/></svg></div>
  </section>

  <!-- Shopping details -->
  <section class="screen" style="left:212px;top:730px">
    <svg class="icon" style="left:13px;top:23px" width="11" height="7" viewBox="0 0 11 7"><path d="M11 3.5H1M3.5 1L1 3.5 3.5 6" fill="none" stroke="#1c2a4b" stroke-width=".9"/></svg>
    <div class="brand"><span class="dot"></span>FIELDLINE</div>
    <svg class="icon" style="left:319px;top:20px" width="13" height="13" viewBox="0 0 13 13"><path d="M1 5h10l-1.3 6H2.3z M3.5 5l2-3.5M8.5 5l-2-3.5" fill="none" stroke="#1c2a4b" stroke-width=".9"/><circle cx="11.5" cy="1.6" r="1.6" fill="#f2395a"/></svg>
    <p class="page-title" style="--line:62px">Shopping Details</p>
    <div class="steps"><span class="step on">1</span><span class="step on">2</span><span class="step">3</span><span class="step">4</span></div>
    <div class="card" style="left:50px;top:73px;width:249px;height:153px">
      <div class="field" style="left:11px;top:10px;width:109px"><label>FIRST NAME<b>••</b></label><span>Karim</span></div>
      <div class="field" style="left:128px;top:10px;width:109px"><label>LAST NAME<b>••</b></label><span>Salvat</span></div>
      <div class="field" style="left:11px;top:39px;width:109px"><label>PHONE NO<b>••</b></label></div>
      <div class="field" style="left:128px;top:39px;width:109px"><label>EMAIL ADDRESS<b>••</b></label></div>
      <div class="field" style="left:11px;top:66px;width:226px"><label>AREA<b>••</b></label></div>
      <div class="field" style="left:11px;top:95px;width:109px"><label>BLOCK<b>••</b></label></div>
      <div class="field" style="left:128px;top:95px;width:109px"><label>STREET<b>••</b></label></div>
      <div class="field" style="left:11px;top:127px;width:189px"><span class="ph">Coupon Code</span></div>
      <div class="abs" style="left:212px;top:127px;width:25px;height:22px;border-radius:3px;background:var(--green);display:flex;align-items:center;justify-content:center">
        <svg width="11" height="9" viewBox="0 0 11 9"><path d="M1 4.5l3 3L10 1" fill="none" stroke="#fff" stroke-width="1.5"/></svg>
      </div>
    </div>
    <div class="btn" style="left:235px;top:235px;width:63px">CHECKOUT<svg viewBox="0 0 10 10"><circle cx="5" cy="5" r="4.3" fill="none" stroke="#fff" stroke-width=".9"/><path d="M3 5h4M5.3 3.3L7 5 5.3 6.7" fill="none" stroke="#fff" stroke-width=".9"/></svg></div>
  </section>

</div>
</body>
</html>
```